Creative Frame Mat for 48Vigor Challenge

I am gifting a present to my wife and am looking for your help to make it happen. I have a 8"x10" picture frame. In it, I want to place a 4"x6" picture. The rest of that space is the creative area I am looking for your help. Let's call it a picture border or mat. I don't care where the 4"x6" cut out for the picture is. You get to decide. The border or mat is to have a #48Vigor theme. Images are below. You can incorporate some/all or add your own design.

Target Market(s)

Gym / health / self help enthusiast

Font styles to use
Sans Serif
Decorative

Requirements
Must have
• - Frame mat is 8" x 10"
- Include a cut out area for a picture to be inserted that is 4" x 6"
- A main header with "48VIGOR"
Nice to have
• Color: Black, grey, white and red
Optional quotes to add in small text:
- I can do more
- Discipline
- Determination
- Perseverance
- Grit
- Confidence
- Self-Belief
- Self-Esteem
- Self-Worth

```html
<!DOCTYPE html>
<html lang="en">
<head>
<meta charset="utf-8">
<title>48Vigor Frame Mat</title>
<link rel="stylesheet" href="https://fonts.googleapis.com/css2?family=Arimo:wght@400;700&display=swap">
<style>
  :root {
    --mat-black: #000000;
    --accent-red: #c8232a;
    --paper-white: #ffffff;
  }
  html, body {
    margin: 0;
    padding: 0;
    overflow: hidden;
    background: var(--mat-black);
  }
  .mat {
    position: relative;
    width: 960px;
    height: 1200px;
    background: var(--mat-black);
    overflow: hidden;
    font-family: "Arimo", Arial, sans-serif;
    color: var(--paper-white);
  }
  .headline {
    position: absolute;
    left: 222px;
    top: 78px;
    margin: 0;
    font-size: 60px;
    line-height: 60px;
    font-weight: 400;
    letter-spacing: 9px;
    white-space: nowrap;
  }
  .headline-rule {
    position: absolute;
    left: 544px;
    top: 142px;
    width: 187px;
    height: 2px;
    background: var(--accent-red);
  }
  .photo-frame {
    position: absolute;
    left: 95px;
    top: 192px;
    width: 770px;
    height: 530px;
  }
  .brand {
    position: absolute;
    left: 64px;
    top: 960px;
    width: 360px;
    display: flex;
    align-items: center;
    gap: 16px;
  }
  .brand-dot {
    width: 26px;
    height: 26px;
    border-radius: 50%;
    background: var(--accent-red);
    flex: none;
  }
  .brand-name {
    margin: 0;
    font-size: 56px;
    line-height: 1;
    font-weight: 700;
    letter-spacing: 2px;
    color: var(--paper-white);
  }
  .values {
    position: absolute;
    left: 566px;
    top: 771px;
    width: 394px;
    margin: 0;
    padding: 0;
    list-style: none;
  }
  .value {
    height: 50.6px;
    box-sizing: border-box;
    padding-top: 0;
    font-size: 29px;
    line-height: 34px;
    letter-spacing: 5px;
    border-bottom: 1.5px solid var(--accent-red);
  }
  .value:last-child {
    border-bottom: none;
  }
</style>
</head>
<body>
  <main class="mat">
    <h2 class="headline">I CAN DO MORE</h2>
    <div class="headline-rule"></div>

    <svg class="photo-frame" viewBox="0 0 770 530" width="770" height="530" aria-label="4 by 6 inch photo opening">
      <rect class="frame-band" x="0" y="0" width="770" height="530" fill="var(--accent-red)"/>
      <rect class="frame-beads" x="13.5" y="11" width="743" height="508" fill="none"
            stroke="var(--paper-white)" stroke-width="4.5" stroke-linecap="round" stroke-dasharray="0 5.2"/>
      <rect class="photo-window" x="26" y="23" width="718" height="480" fill="var(--paper-white)"/>
    </svg>

    <div class="brand">
      <span class="brand-dot"></span>
      <h1 class="brand-name">48VIGOR</h1>
    </div>

    <ul class="values">
      <li class="value">DISCIPLINE</li>
      <li class="value">DETERMINATION</li>
      <li class="value">PERSEVERANCE</li>
      <li class="value">GRIT</li>
      <li class="value">CONFIDENCE</li>
      <li class="value">SELF-BELIEF</li>
      <li class="value">SELF-ESTEEM</li>
      <li class="value">SELF-WORTH</li>
    </ul>
  </main>
</body>
</html>
```